Brochure Design Project

Looking to have a 3 panel (folded) brochure designed for our business.

take inspiration/colorschemes from our upcoming site: www.velqorstudio.ca/demo

photos and ideas from: www.facebook.com/velqorstudiocanada

Lots of new photos uploaded this morning!

New Fonts added to match with our branding. Please use for all main text/headings.

New photo uploaded called 'small'

Please incorporate it into design.

Target Market(s)

Wealthy Home Owners

Industry/Entity Type

Business

Requirements
Must have
• 3 inside panels detail : Home Automation Services (2 of 3 panels) and Home Theater Services (1 of 3 panels).

```html
<!DOCTYPE html>
<html lang="en">
<head>
<meta charset="utf-8">
<title>Velqor Studio – Home Automation &amp; Home Theater Brochure</title>
<link rel="stylesheet" href="https://fonts.googleapis.com/css2?family=Roboto+Slab:wght@400&family=Nunito+Sans:wght@400;600&display=swap">
<style>
  :root {
    --slate: #5e6267;
    --slate-dark: #55595e;
    --header-black: #151617;
    --heading-grey: #9c9d9f;
    --gold: #c9a04a;
    --text-light: #eceded;
    --divider: #787c81;
  }
  * { margin: 0; padding: 0; box-sizing: border-box; }
  html, body { width: 1200px; height: 927px; overflow: hidden; background: var(--slate); }
  .brochure {
    position: relative;
    width: 1200px; height: 927px;
    background: var(--slate);
    font-family: "Nunito Sans", Arial, sans-serif;
    color: var(--text-light);
    overflow: hidden;
  }
  .top-strip { position: absolute; left: 0; top: 0; width: 1200px; height: 61px; background: var(--slate-dark); }
  .header-band { position: absolute; left: 0; top: 61px; width: 1200px; height: 116px; background: var(--header-black); }
  .gold-rule { position: absolute; left: 0; top: 177px; width: 1200px; height: 6px; background: var(--gold); }
  .panel-divider { position: absolute; top: 0; width: 1px; height: 927px; background: var(--divider); opacity: .7; }
  .panel-heading {
    position: absolute; top: 98px;
    font-family: "Roboto Slab", Georgia, serif;
    font-weight: 400; font-size: 31px; letter-spacing: .5px;
    color: var(--heading-grey);
  }
  .photo { position: absolute; }
  .photo-rack { left: 0; top: 183px; width: 259px; height: 340px;
    background: linear-gradient(160deg, #1c2a3d 0%, #0b0f17 55%, #3a2a1e 100%); }
  .photo-house { left: 259px; top: 183px; width: 541px; height: 340px;
    background: linear-gradient(180deg, #1d2c4a 0%, #3b4a66 45%, #6b5a44 75%, #2a2620 100%); }
  .photo-remote { left: 674px; top: 205px; width: 111px; height: 295px; border-radius: 22px;
    background: linear-gradient(180deg, #2b2e33 0%, #0e0f11 100%); }
  .photo-theater { left: 800px; top: 183px; width: 400px; height: 340px;
    background: linear-gradient(180deg, #2a1e16 0%, #5a3b25 50%, #1a1411 100%); }
  .body-copy { position: absolute; font-size: 15.5px; line-height: 21px; }
  .body-copy p + p { margin-top: 21px; }
  .feature-list {
    position: absolute; list-style: none;
    display: grid; grid-template-columns: repeat(2, auto); column-gap: 26px; row-gap: 3px;
    font-size: 15.5px; line-height: 21px;
  }
  .feature-list li::before { content: "•"; margin-right: 9px; }
  .services-list li { font-weight: 600; }
  .device { position: absolute; }
  .device-tablet { left: 429px; top: 753px; width: 101px; height: 138px; border-radius: 6px;
    background: linear-gradient(180deg, #1e2c44 0%, #0d1320 100%); border: 5px solid #1a1a1a; }
  .device-phone { left: 542px; top: 826px; width: 31px; height: 68px; border-radius: 5px;
    background: linear-gradient(180deg, #24385a 0%, #0e1524 100%); border: 3px solid #111; }
  .device-panel { left: 588px; top: 758px; width: 185px; height: 133px; border-radius: 3px;
    background: linear-gradient(180deg, #f4f5f6 0%, #d9dde2 100%); }
  .thumb { position: absolute; top: 542px; width: 161px; height: 132px; border: 6px solid var(--gold); }
  .thumb-media-room { left: 830px; background: linear-gradient(180deg, #5a4636 0%, #2a211b 100%); }
  .thumb-star-ceiling { left: 1009px; background: linear-gradient(180deg, #0d1a33 0%, #3a2416 100%); }
</style>
</head>
<body>
<main class="brochure">
  <div class="top-strip"></div>
  <div class="header-band"></div>
  <div class="gold-rule"></div>

  <h1 class="panel-heading" style="left:30px;">HOME AUTOMATION</h1>
  <h1 class="panel-heading" style="left:830px;">HOME THEATER</h1>

  <div class="photo photo-rack" role="img" aria-label="Equipment rack with blue-lit audio and network components"></div>
  <div class="photo photo-house" role="img" aria-label="Luxury home exterior lit at dusk"></div>
  <div class="photo photo-remote" role="img" aria-label="Handheld touchscreen remote control"></div>
  <div class="photo photo-theater" role="img" aria-label="Dedicated home theater room with projection screen and leather seating"></div>

  <section class="body-copy" style="left:30px; top:541px; width:350px;">
    <p>Home Automation is the combination of all of the building’s systems into one easy-to-use interface that is quick to navigate and simple to learn. Whether you are building a multi-million dollar estate, a spec home, or a doing a simple renovation, Home Automation technology will enhance any living space.</p>
    <p>Velqor Studio’s Custom-Designed Home Automation System Can Control:</p>
  </section>
  <ul class="feature-list" style="left:30px; top:786px;">
    <li>Lighting</li><li>Pool/Spa</li>
    <li>Security</li><li>CCTV</li>
    <li>Audio/Video</li><li>Gates/Garage Door</li>
    <li>Climate</li>
  </ul>

  <section class="body-copy" style="left:430px; top:541px; width:345px;">
    <p>Imagine driving up to your home on a rainy Vancouver evening. As you approach, you open up our Smartphone application and press ‘Arrive’. Instantly, the gates and garage door open, the lights turn on, the security system disarms, and the heat in the home rises by 3 degrees. This is no longer science-fiction, this is a Velqor Studio Home Automation System.</p>
  </section>
  <div class="device device-tablet" role="img" aria-label="Tablet showing the home control app"></div>
  <div class="device device-phone" role="img" aria-label="Smartphone showing the home control app"></div>
  <div class="device device-panel" role="img" aria-label="Wall-mounted touch panel with home control icons"></div>

  <div class="thumb thumb-media-room" role="img" aria-label="Media room with wall-mounted screen"></div>
  <div class="thumb thumb-star-ceiling" role="img" aria-label="Theater with star-lit ceiling"></div>
  <section class="body-copy" style="left:830px; top:693px; width:345px;">
    <p>We design and install Home Theaters and Media Rooms that amaze! Whether you have a dedicated room or a multi-purpose space, we can engineer a system that truly brings the cinema experience home to you.</p>
    <p>Our Services Include:</p>
  </section>
  <ul class="feature-list services-list" style="left:830px; top:842px; column-gap:34px;">
    <li>Design</li><li>Soundproofing</li>
    <li>Installation</li><li>Calibration</li>
  </ul>

  <div class="panel-divider" style="left:400px;"></div>
  <div class="panel-divider" style="left:800px;"></div>
</main>
</body>
</html>
```